Healer at the Hearth needs business card

We need a business card that reflects the look and feel of the new website at www.healerathearth.ca

Target Market(s)

Our patient navigation and advocacy services are most commonly used by seniors who feel overwhelmed by the health care system and want someone on their side to advocate for their care. Individuals with ill parents or other family members may also come to rely on Healer at the Hearth to help them support their loved one through their health care journey. Ultimately, anyone who finds their health care experience challenging and wants someone completely focused on their needs can benefit from the services of our doctor / nurse team.

Industry/Entity Type

Business

Requirements
Must have
• One design tailored for two clinician which should include: logo, name, title, tel, email, web address and tagline
Nice to have
• A banner image to create a similar look to the website at www.healerathearth.ca
Should not have
• Too cluttered or busy - must be clean and professional

```html
<!DOCTYPE html>
<html lang="en">
<head>
<meta charset="utf-8">
<title>Healer at the Hearth – business card landscape designs</title>
<link rel="stylesheet" href="https://fonts.googleapis.com/css2?family=Lato:wght@300;400;700&display=swap">
<style>
  :root {
    --ink: #1a1a1a;
    --brand-blue: #2d5286;
    --brand-red: #a51d24;
    --card-border: #b9b9b9;
    --sand: #d9d4b8;
    --sand-light: #eeebe3;
    --linen: #e9e3d7;
    --linen-deep: #e4e0d2;
    --slate: #cdd1de;
    --blush: #f0ddd5;
    --tagline-bg: #ececE4;
    --sepia-1: #e6dccd;
    --sepia-2: #b9a995;
    --grey-1: #d8d8d8;
    --grey-2: #8c8c8c;
    --clinic-1: #e6f0f7;
    --clinic-2: #3fb2a4;
  }
  * { box-sizing: border-box; margin: 0; padding: 0; }
  html, body { width: 1200px; height: 927px; overflow: hidden; background: #fff; }
  body { position: relative; font-family: "Lato", sans-serif; color: var(--ink); }

  .sheet-title {
    position: absolute; left: 36px; top: 28px;
    font-size: 27px; font-weight: 300; letter-spacing: -0.2px;
  }

  .card {
    position: absolute; width: 382px; height: 218px;
    overflow: hidden; background: #fff;
    border: 1px solid var(--card-border);
  }
  .card--left { left: 177px; }
  .card--right { left: 649px; }
  .row-1 { top: 129px; }
  .row-2 { top: 365px; }
  .row-3 { top: 601px; }

  .block { position: absolute; }
  .photo { position: absolute; }

  /* brand name lockup */
  .brand { position: absolute; display: flex; align-items: center; gap: 7px; }
  .brand-dot { width: 26px; height: 26px; border-radius: 50%; background: var(--brand-red); flex: none; }
  .brand-name {
    font-weight: 400; color: var(--brand-blue);
    font-size: 17px; line-height: 1.05;
  }
  .brand--large .brand-dot { width: 46px; height: 46px; }
  .brand--large .brand-name { font-size: 24px; }

  .person-name { font-size: 21px; font-weight: 400; }
  .person-title { font-size: 12px; }
  .contact { font-size: 15px; line-height: 1.4; }
  .contact small { font-size: 9px; }
  .contact .web { font-weight: 700; }

  /* card 1 front */
  .tagline {
    position: absolute; left: 110px; top: 102px; width: 150px; height: 36px;
    background: var(--tagline-bg);
    display: flex; align-items: center; justify-content: center; text-align: center;
    font-size: 11px; line-height: 1.2; color: var(--brand-blue); text-transform: uppercase;
  }
  .sepia { background: linear-gradient(150deg, var(--sepia-1), var(--sepia-2)); }

  /* card 2/3 photo fronts */
  .photo--grey { inset: 0; background: linear-gradient(120deg, var(--grey-1) 0%, var(--grey-2) 55%, #e6e6e6 100%); }
  .photo--clinic { inset: 0; background: linear-gradient(110deg, var(--clinic-1) 0%, var(--clinic-2) 38%, #f3f3f3 60%, #dcc1ae 100%); }
  .brand--onphoto { left: 20px; bottom: 22px; }
  .brand--onphoto .brand-name { color: #fff; font-size: 19px; width: 110px; }
  .brand--onphoto .brand-dot { width: 34px; height: 34px; }
</style>
</head>
<body>

<h1 class="sheet-title">Healer at the Hearth - business card landscape designs</h1>

<!-- Design 1 : front -->
<section class="card card--left row-1">
  <div class="photo sepia" style="left:0;top:0;width:167px;height:100px" role="img" aria-label="Photo of a doctor with a stethoscope"></div>
  <div class="photo sepia" style="left:171px;top:0;width:117px;height:100px" role="img" aria-label="Photo of a smiling senior woman holding a heart"></div>
  <div class="photo sepia" style="left:291px;top:0;width:91px;height:100px" role="img" aria-label="Photo of clasped caring hands"></div>
  <div class="photo sepia" style="left:0;top:102px;width:107px;height:116px" role="img" aria-label="Photo of a young woman smiling"></div>
  <div class="tagline">Patient Navigation &amp;<br>Advocacy Services</div>
  <div class="photo sepia" style="left:110px;top:139px;width:150px;height:79px" role="img" aria-label="Photo of a smiling senior man"></div>
  <div class="photo sepia" style="left:263px;top:139px;width:73px;height:79px" role="img" aria-label="Photo of a hand working a calculator"></div>
  <div class="block" style="left:336px;top:139px;width:46px;height:48px;background:#fff;display:flex;align-items:center;justify-content:center">
    <span class="brand-dot" style="width:24px;height:24px;border-radius:50%;background:var(--brand-red)"></span>
  </div>
  <div class="block" style="left:336px;top:187px;width:46px;height:31px;background:var(--sand-light)"></div>
</section>

<!-- Design 1 : back -->
<section class="card card--right row-1">
  <div class="brand" style="left:15px;top:24px">
    <span class="brand-dot"></span>
    <span class="brand-name">Healer at<br>the Hearth</span>
  </div>
  <div class="block" style="left:0;top:81px;width:251px;height:47px;background:var(--sand);display:flex;align-items:center;padding-left:21px">
    <span class="person-name">Marcus Fenwell</span>
  </div>
  <div class="block" style="left:255px;top:81px;width:127px;height:47px;background:var(--slate);padding:9px 0 0 9px">
    <span class="person-title">MD and<br>Co-Founder</span>
  </div>
  <div class="block" style="left:0;top:131px;width:55px;height:87px;background:var(--sand-light)"></div>
  <div class="block contact" style="left:58px;top:131px;width:324px;height:87px;background:var(--blush);padding:4px 0 0 8px">
    <div><small>Tel:</small> 555-014-2380</div>
    <div style="font-size:13px"><small>Email:</small> info@healerathearth.ca</div>
    <div class="web">www.healerathearth.ca</div>
  </div>
</section>

<!-- Design 2 : front -->
<section class="card card--left row-2">
  <div class="photo photo--grey" role="img" aria-label="Black and white photo of a doctor holding a patient's hands"></div>
  <div class="brand brand--onphoto">
    <span class="brand-dot"></span>
    <span class="brand-name">Healer at the Hearth</span>
  </div>
</section>

<!-- Design 2 : back -->
<section class="card card--right row-2">
  <div class="brand" style="left:12px;top:78px">
    <span class="brand-dot"></span>
    <span class="brand-name">Healer at<br>the Hearth</span>
  </div>
  <div class="block" style="left:147px;top:0;width:235px;height:218px;background:var(--linen);padding:70px 0 0 12px">
    <div class="person-name">Marcus Fenwell</div>
    <div class="person-title" style="margin-bottom:14px">MD and Co-Founder</div>
    <div class="contact">
      <div><small>Tel:</small> 555-014-2380</div>
      <div style="font-size:13px"><small>Email:</small> info@healerathearth.ca</div>
      <div class="web">www.healerathearth.ca</div>
    </div>
  </div>
</section>

<!-- Design 3 : front -->
<section class="card card--left row-3">
  <div class="photo photo--clinic" role="img" aria-label="Colour photo of a doctor in a white coat holding a patient's hands"></div>
  <div class="brand brand--onphoto">
    <span class="brand-dot"></span>
    <span class="brand-name">Healer at the Hearth</span>
  </div>
</section>

<!-- Design 3 : back -->
<section class="card card--right row-3">
  <div class="block" style="right:229px;top:36px;text-align:right">
    <div class="person-name" style="font-size:17px">Marcus Fenwell</div>
    <div class="person-title" style="font-size:9px">MD and Co-Founder</div>
  </div>
  <div class="block contact" style="left:176px;top:32px;font-size:13px;line-height:1.5">
    <div><small>Tel:</small> 555-014-2380</div>
    <div style="font-size:12px"><small>Email:</small> info@healerathearth.ca</div>
    <div style="font-size:12px">www.healerathearth.ca</div>
  </div>
  <div class="block" style="left:0;top:108px;width:382px;height:110px;background:var(--linen-deep);display:flex;align-items:center;justify-content:center">
    <div class="brand brand--large" style="position:static">
      <span class="brand-dot"></span>
      <span class="brand-name">Healer at<br>the Hearth</span>
    </div>
  </div>
</section>

</body>
</html>
```